Velmont Recycling needs a new web design

We need a new web design for our company based in Austin, TX. We resell and recycling electronics such as laptops, computer components, Zelvos, Quorbs, etc. Since our inception over ten years ago, we’ve become one of the premier electronics recycling and remarketing companies in Austin, Texas.

```html
<!DOCTYPE html>
<html lang="en">
<head>
<meta charset="utf-8">
<title>Velmont Recycling</title>
<link rel="stylesheet" href="https://fonts.googleapis.com/css2?family=Arimo:ital,wght@0,400;0,700;1,400&family=Noto+Serif:wght@400;700&display=swap">
<style>
:root{
  --blue:#2a6ebb;
  --blue-dark:#1f5da3;
  --footer:#3475b7;
  --strip:#1d9079;
  --green:#0aa84b;
  --text:#444;
  --grey:#555;
  --map:#dbe8f6;
  --white:#fff;
}
*{margin:0;padding:0;box-sizing:border-box}
html,body{width:1200px;height:1200px;overflow:hidden;background:var(--white)}
body{font-family:"Arimo",Arial,sans-serif;color:var(--text)}
.stage{position:absolute;left:0;top:0;width:1500px;height:1500px;transform:scale(.8);transform-origin:0 0}
.abs{position:absolute}
.brand{left:625px;top:5px;display:flex;align-items:center;gap:6px}
.brand-dot{width:26px;height:26px;border-radius:50%;background:var(--blue-dark)}
.brand-name{font-family:"Noto Serif",serif;font-weight:700;font-size:15px;color:var(--blue-dark)}
.nav{left:808px;top:14px;display:flex;gap:7px;font-family:"Noto Serif",serif;font-size:8.5px;color:#333}
.nav .active{color:var(--blue)}
.map{left:415px;top:40px;width:670px;height:330px;background:radial-gradient(ellipse at 50% 45%,var(--map),rgba(219,232,246,.25) 70%,transparent)}
.hero-title{left:600px;width:325px;top:120px;text-align:center;color:var(--blue);font-weight:700;font-size:17px;line-height:20px}
.hero-copy{left:636px;width:264px;top:166px;text-align:center;font-size:9.5px;line-height:12.3px;color:var(--grey)}
.btn{position:absolute;background:var(--green);color:var(--white);font-weight:700;text-align:center;display:flex;align-items:center;justify-content:center}
.btn-learn{left:713px;top:246px;width:95px;height:22px;font-size:11px}
.btn-pickup{width:152px;height:40px;font-size:13px;line-height:16px;box-shadow:2px 2px 3px rgba(0,0,0,.35)}
.art{position:absolute}
.recycle-mark{left:700px;top:352px;width:122px;height:120px;border-radius:50%;background:radial-gradient(circle,#3f8ad6,#2f7ccc)}
.bin{left:550px;top:485px;width:175px;height:145px;background:linear-gradient(160deg,#6aa7dc,#3a86cc 60%,#e4e8ee);border-radius:8px}
.truck{left:800px;top:500px;width:195px;height:118px;background:linear-gradient(170deg,#8b9fb8,#3d4d63 65%,#e6e9ee);border-radius:10px}
.svc{position:absolute;width:280px;text-align:center}
.svc h2{color:var(--blue);font-size:14px;font-weight:700}
.svc h3{font-style:italic;font-weight:400;font-size:14px;color:var(--grey);margin-top:6px}
.svc p{font-size:10px;line-height:12.4px;color:var(--grey)}
.about-title{left:529px;top:917px;font-size:17px;font-weight:700;color:var(--blue)}
.about-copy{left:529px;top:948px;width:495px;font-size:13.5px;line-height:16.3px;color:#333}
.footer{left:413px;top:1127px;width:674px;height:343px;background:var(--footer)}
.strip{left:413px;top:1470px;width:674px;height:30px;background:var(--strip);font-size:10px;color:#1a2d2a}
.strip .copy{position:absolute;left:68px;top:8px}
.strip .links{position:absolute;left:367px;top:8px;display:flex;gap:9px}
.f-title{color:var(--white);font-size:16px;font-weight:700}
.f-text{color:var(--white);font-size:13px;line-height:16px}
.field{position:absolute;left:822px;width:226px;background:#f4f7fa;font-size:10px;color:#222;padding:8px 6px}
.submit{left:935px;top:1413px;width:112px;height:30px;font-size:13px}
.social{position:absolute;width:40px;height:40px;border-radius:50%}
</style>
</head>
<body>
<div class="stage">
  <div class="abs brand"><span class="brand-dot"></span><span class="brand-name">VELMONT</span></div>
  <nav class="abs nav"><span class="active">HOME</span><span>ABOUT US</span><span>SERVICES</span><span>BOOK ONLINE</span><span>CONTACT US</span></nav>

  <div class="abs map" role="img" aria-label="Dotted world map in pale blue"></div>
  <h1 class="abs hero-title">COMPUTER RECYCLING<br>MADE EASY</h1>
  <p class="abs hero-copy">Want to make a difference to our environment and planet? Velmont Recycling is here to help! Velmont recycling has been helping keep the environment healthy since 2006, we specialize in recycling services that help citizens become experts at reducing waste. We have a passion to</p>
  <div class="btn btn-learn">Learn More</div>

  <svg class="abs" style="left:413px;top:290px" width="674" height="150" viewBox="0 0 674 150">
    <path d="M0,14 C90,70 190,105 290,112 L674,118" fill="none" stroke="#c9ccd1" stroke-width="5"/>
    <path d="M0,6 C90,62 190,97 290,104 L400,104 C500,103 600,100 674,108" fill="none" stroke="var(--blue)" stroke-width="4"/>
  </svg>
  <div class="art recycle-mark" role="img" aria-label="Large blue recycling arrows emblem"></div>

  <div class="art bin" role="img" aria-label="Illustration of a blue recycling bin filled with electronic devices"></div>
  <div class="art truck" role="img" aria-label="Photo of a pickup truck with a covered camper shell"></div>

  <div class="svc" style="left:486px;top:667px">
    <h2>ELECTRONIC RECYCLING</h2>
    <h3>Environmentally Friendly</h3>
    <p>At Velmont Recycling, we strive to keep the environment clean through our wide range of services. Our E-Waste Recycling services were designed to simplify the recycling process for residents in the Austin area. Contact us today and see how you can contribute to making this world a cleaner place.</p>
  </div>
  <div class="svc" style="left:778px;top:667px">
    <h2>RECYCLING PICK UP</h2>
    <h3>We Come To You</h3>
    <p>At Velmont Recycling, we go out of our way to make sure your recycling process is made easy as possible. Our Recycling Pickup service is designed to simplify all of your recycling needs . Take a look at all the services we offer and get in touch to see how you can start the process today!</p>
  </div>
  <div class="btn btn-pickup" style="left:561px;top:829px">Schedule a<br>pickup</div>
  <div class="btn btn-pickup" style="left:846px;top:829px">Schedule a<br>pickup</div>

  <h2 class="abs about-title">ABOUT US</h2>
  <p class="abs about-copy">At Velmont Recycling, we’re committed to providing environmentally friendly recycling solutions to Austin and the surrounding areas. Founded in 2006, our mission is to process your materials in a safe, non-hazardous manner — with an aim to keep the world environmentally clean. As a R2 recycling center, we believe in promoting smart recycling habits in order to achieve long lasting results.</p>
  <div class="btn btn-pickup" style="left:697px;top:1064px">Schedule a<br>pickup</div>

  <footer>
    <div class="abs footer"></div>
    <h2 class="abs f-title" style="left:505px;top:1169px">VISIT US</h2>
    <svg class="abs" style="left:463px;top:1200px" width="26" height="38" viewBox="0 0 26 38"><path d="M13,1 C6,1 1,6 1,13 C1,22 13,37 13,37 C13,37 25,22 25,13 C25,6 20,1 13,1 Z M13,8 A5,5 0 1 1 12.9,8 Z" fill="#111" fill-rule="evenodd"/></svg>
    <p class="abs f-text" style="left:505px;top:1204px">4120 Maple Ridge Blvd.<br>Austin, Texas 78701</p>
    <svg class="abs" style="left:463px;top:1249px" width="36" height="34" viewBox="0 0 36 34"><path d="M4,2 L11,1 L15,9 L11,13 C14,19 18,23 24,26 L28,22 L35,26 L34,32 C20,34 3,20 4,2 Z" fill="#111"/></svg>
    <p class="abs f-text" style="left:505px;top:1253px">(512)555-0148 Cell<br>(512)555-0173 Fax<br>(844)55-VELMO (83566) Toll Free</p>
    <svg class="abs" style="left:461px;top:1313px" width="37" height="26" viewBox="0 0 37 26"><rect x="1.5" y="1.5" width="34" height="23" fill="none" stroke="#111" stroke-width="3"/><path d="M2,2 L18.5,15 L35,2 M2,24 L14,12 M35,24 L23,12" fill="none" stroke="#111" stroke-width="2.5"/></svg>
    <p class="abs f-text" style="left:505px;top:1318px">Dana@VelmontRecycling.com</p>
    <span class="social" style="left:460px;top:1373px;background:#5d7fc0"></span>
    <span class="social" style="left:508px;top:1373px;background:#3fb5ef"></span>
    <span class="social" style="left:557px;top:1373px;background:#d8281f"></span>

    <h2 class="abs f-title" style="left:895px;top:1173px">CONTACT US</h2>
    <div class="field" style="top:1207px;height:33px">NAME</div>
    <div class="field" style="top:1248px;height:33px;padding-top:12px">EMAIL</div>
    <div class="field" style="top:1290px;height:92px">MESSAGE</div>
    <div class="btn submit">SUBMIT</div>

    <div class="abs strip">
      <span class="copy">COPY RIGHT 2018 ALL RIGHTS RESERVED</span>
      <span class="links"><span>ABOUT US</span><span>SERVICES</span><span>PRIVACY POLICY</span><span>TERMS</span></span>
    </div>
  </footer>
</div>
</body>
</html>
```